Bramble Roofing Website Relaunch

We require a re-launch of our website, We are a longrun roofing company based in New Zealand, we are rapidly expanding and require a more professionally presented website our current website is www.brambleroofing.co.nz we want something modern, masculine and communicates a "strong" "superior" image, we already have a logo which I have attached we use the orange and silver one as you will see on our current website

Industry/Entity Type

It Company

Number of Pages Required

1 page

Colors
f37122
f78f20
000000
1b1b1b
474747
d3d3d3
f5f5f5

Requirements
Must have
• Images of our work
• Email and Mobile Contact Details
• Link to Facebook page
• Who We Are, What We Do
• Certified Trade Craftsman Logo
• Our Logo

```html
<!DOCTYPE html>
<html lang="en">
<head>
<meta charset="utf-8">
<title>Bramble Roofing</title>
<link href="https://fonts.googleapis.com/css2?family=Open+Sans:wght@400;600;700;800&display=swap" rel="stylesheet">
<style>
:root{
  --orange:#f37122;
  --orange-light:#f78f20;
  --black:#000000;
  --ink:#1b1b1b;
  --charcoal:#474747;
  --silver:#d3d3d3;
  --paper:#f5f5f5;
  --band:#eeeef0;
  --white:#ffffff;
  --body:#555555;
}
*{box-sizing:border-box;margin:0;padding:0}
html,body{width:1200px;height:2597px;overflow:hidden}
body{position:relative;background:var(--white);font-family:'Open Sans',Arial,sans-serif;color:var(--ink)}

/* header */
.site-header{position:absolute;left:0;top:0;width:1200px;height:121px;background:var(--white)}
.brand{position:absolute;left:133px;top:30px;display:flex;align-items:center;gap:14px}
.brand-mark{width:44px;height:44px;background:var(--silver)}
.brand-name{font-weight:800;font-size:30px;color:var(--orange);letter-spacing:.5px;line-height:1}
.header-call{position:absolute;left:866px;top:26px;display:flex;align-items:center;gap:14px}
.header-call .icon{width:36px;height:36px;border-radius:50%;background:var(--orange);display:flex;align-items:center;justify-content:center}
.header-call small{display:block;font-size:11px;font-weight:700;color:var(--charcoal)}
.header-call strong{display:block;font-size:21px;font-weight:800;color:var(--orange);line-height:1.1}
.main-nav{position:absolute;top:81px;left:495px;height:33px;display:flex;align-items:center}
.main-nav a{font-size:11.5px;font-weight:700;color:var(--charcoal);text-decoration:none;text-transform:uppercase;padding:0 19px;height:33px;line-height:33px}
.main-nav a.active{background:var(--orange);color:var(--white);padding:0 13px}
.main-nav a.who{margin-left:6px}
.main-nav a:last-child{padding-right:0}

/* hero */
.hero{position:absolute;left:0;top:121px;width:1200px;height:549px;
  background:linear-gradient(180deg,#6d7479 0%,#8b9196 35%,#5e6266 55%,#6b5a45 80%,#4f5a34 100%)}
.hero h1{position:absolute;top:196px;width:100%;text-align:center;font-size:48px;font-weight:800;color:var(--white);letter-spacing:1px}
.hero p{position:absolute;top:256px;width:100%;text-align:center;font-size:21px;color:var(--white)}
.hero-dots{position:absolute;top:484px;left:0;width:100%;display:flex;justify-content:center;gap:14px}
.hero-dots span{width:10px;height:10px;border-radius:50%;background:var(--white)}
.hero-dots span.on{background:transparent;border:2px solid var(--white);width:12px;height:12px;margin-top:-1px}

/* welcome */
.welcome h2{position:absolute;left:135px;top:728px;font-size:29px;font-weight:800;color:var(--orange)}
.welcome p{position:absolute;left:135px;top:788px;width:455px;font-size:13px;line-height:21px;color:var(--body);text-align:justify}
.btn{position:absolute;left:137px;top:933px;width:130px;height:42px;background:var(--orange);color:var(--white);font-size:13px;font-weight:700;text-transform:uppercase;text-align:center;line-height:42px;text-decoration:none}
.welcome-art{position:absolute;left:655px;top:630px}

/* services */
.services{position:absolute;left:0;top:1025px;width:1200px;height:663px;background:var(--band)}
.section-title{position:absolute;font-size:29px;font-weight:800;color:var(--orange);text-transform:uppercase}
.tile{position:absolute;width:303px;height:221px;overflow:hidden}
.tile .photo{position:absolute;inset:0}
.tile .caption{position:absolute;left:0;bottom:0;width:100%;height:42px;background:rgba(27,27,27,.78);color:var(--white);font-size:14px;font-weight:700;line-height:42px;padding-left:14px}

/* work */
.work-photo{position:absolute;top:1836px;width:300px;height:247px}
.work-title{position:absolute;top:2097px;width:300px;text-align:center;font-size:14.5px;font-weight:700;color:var(--orange)}
.work-arrows{position:absolute;left:1012px;top:1760px;display:flex;gap:12px}

/* footer */
.site-footer{position:absolute;left:0;top:2178px;width:1200px;height:419px;background:var(--charcoal);color:var(--white)}
.foot-label{position:absolute;font-size:13.5px;font-weight:700;color:var(--orange);text-transform:uppercase}
.contact-item{position:absolute;top:90px;display:flex;gap:18px;align-items:flex-start}
.contact-item small{display:block;font-size:11px;color:var(--white)}
.contact-item span{display:block;font-size:19px;color:var(--white);margin-top:2px}
.foot-menu{position:absolute;left:133px;top:218px;font-size:11.5px;color:var(--white)}
.foot-menu a{color:var(--white);text-decoration:none}
.foot-menu i{font-style:normal;margin:0 7px}
.badge{position:absolute;left:880px;top:47px;width:190px;height:190px;border-radius:50%;border:6px solid #2b2b2b;background:#3a3a3a}
.foot-rule{position:absolute;left:133px;top:281px;width:934px;height:1px;background:#5d5d5d}
.foot-brand{position:absolute;left:133px;top:325px;display:flex;align-items:center;gap:10px}
.foot-brand .brand-mark{width:30px;height:30px}
.foot-brand .brand-name{font-size:19px}
.follow{position:absolute;left:376px;top:334px;display:flex;align-items:center;gap:16px;font-size:14px;font-weight:700;color:var(--orange)}
.follow .social{width:28px;height:28px;border-radius:50%;background:var(--silver)}
.copyright{position:absolute;right:133px;top:341px;font-size:11px;color:var(--white)}
</style>
</head>
<body>

<header class="site-header">
  <div class="brand"><span class="brand-mark"></span><span class="brand-name">Bramble Roofing</span></div>
  <div class="header-call">
    <span class="icon"><svg width="18" height="18" viewBox="0 0 24 24"><path fill="#fff" d="M6.6 10.8a15 15 0 006.6 6.6l2.2-2.2c.3-.3.7-.4 1-.2 1.1.4 2.3.6 3.6.6.6 0 1 .4 1 1V20c0 .6-.4 1-1 1C10.6 21 3 13.4 3 4c0-.6.4-1 1-1h3.5c.6 0 1 .4 1 1 0 1.3.2 2.5.6 3.6.1.3 0 .7-.2 1z"/></svg></span>
    <div><small>CALL US</small><strong>021 555 01234</strong></div>
  </div>
  <nav class="main-nav">
    <a class="active" href="#">Home</a>
    <a class="who" href="#">Who We Are</a>
    <a href="#">What We Do</a>
    <a href="#">Services</a>
    <a href="#">Our Work</a>
    <a href="#">Contact Us</a>
  </nav>
</header>

<section class="hero" role="img" aria-label="Photo of a new house with a dark longrun roof surrounded by scaffolding under a cloudy sky">
  <h1>ROOFING</h1>
  <p>Lorem Ipsum is simply dummy text of the printing</p>
  <div class="hero-dots"><span></span><span class="on"></span><span></span><span></span><span></span></div>
</section>

<section class="welcome">
  <h2>WELCOME TO OUR SITE</h2>
  <p>We are a local, family owned and operated company with over 18 years extensive experience in the roofing industry, Roofing not only Waikato and Auckland but surrounding areas also. We are committed to providing superior service to our customers regardless of how big or small your project is, Your satisfaction is our guarantee.</p>
  <a class="btn" href="#">Read More</a>
  <svg class="welcome-art" width="350" height="360" viewBox="0 0 350 360">
    <defs>
      <linearGradient id="diamondFill" x1="0" y1="0" x2="0" y2="1">
        <stop offset="0" stop-color="#7fb1de"/><stop offset=".55" stop-color="#c9d0d6"/><stop offset="1" stop-color="#6f8a4c"/>
      </linearGradient>
    </defs>
    <polygon points="173,2 345,178 173,354 1,178" fill="#fff" stroke="#e2e2e2"/>
    <polygon points="173,12 335,178 173,344 11,178" fill="url(#diamondFill)" role="img" aria-label="Photo of a weatherboard house with a new dark roof"/>
    <rect x="58" y="236" width="78" height="78" fill="#fff"/>
    <rect x="62" y="240" width="70" height="70" fill="#7c9a6a" role="img" aria-label="Photo of a finished house on a lawn"/>
    <rect x="247" y="194" width="80" height="80" fill="#fff"/>
    <rect x="251" y="198" width="72" height="72" fill="#a7b4c2" role="img" aria-label="Photo of a house under construction"/>
  </svg>
</section>

<section class="services">
  <h2 class="section-title" style="left:132px;top:60px">Our Services</h2>
  <div class="tile" style="left:133px;top:139px"><div class="photo" role="img" aria-label="Photo of a steel roof frame under blue sky" style="background:linear-gradient(180deg,#4f86c9,#9bb7d4 60%,#6f8c4e)"></div><div class="caption">New Roofs and Re-roofs</div></div>
  <div class="tile" style="left:448px;top:139px"><div class="photo" role="img" aria-label="Photo of metal cladding sheets on a roof" style="background:linear-gradient(180deg,#8eb0d2,#3d4652 45%,#262a30)"></div><div class="caption">Metal Cladding</div></div>
  <div class="tile" style="left:764px;top:139px"><div class="photo" role="img" aria-label="Photo of roof spouting and metal fascia" style="background:linear-gradient(160deg,#9aa6a0,#3a3e42 50%,#777d80)"></div><div class="caption">Spouting and Metal Fascia</div></div>
  <div class="tile" style="left:133px;top:374px"><div class="photo" role="img" aria-label="Photo of a white downpipe on a brick wall" style="background:linear-gradient(160deg,#b24a35,#d9d6d2 45%,#a9573e)"></div><div class="caption">Down Pipes</div></div>
  <div class="tile" style="left:448px;top:374px"><div class="photo" role="img" aria-label="Photo of a house alteration site with a ute" style="background:linear-gradient(180deg,#c7ccd2,#8a8f94 50%,#4a4c4e)"></div><div class="caption">Alterations</div></div>
  <div class="tile" style="left:764px;top:374px"><div class="photo" role="img" aria-label="Photo of a dark roof extension" style="background:linear-gradient(180deg,#8a8670,#4a4b4d 40%,#2f3133)"></div><div class="caption">Extensions</div></div>
</section>

<section class="work">
  <h2 class="section-title" style="left:128px;top:1754px">Our Work</h2>
  <div class="work-arrows">
    <svg width="22" height="30" viewBox="0 0 22 30"><path d="M17 3L5 15l12 12" fill="none" stroke="#9a9a9a" stroke-width="3"/></svg>
    <svg width="22" height="30" viewBox="0 0 22 30"><path d="M5 3l12 12L5 27" fill="none" stroke="#9a9a9a" stroke-width="3"/></svg>
  </div>
  <div class="work-photo" style="left:132px;background:linear-gradient(180deg,#b8c3cf,#5b5f66 45%,#b7b2ac)" role="img" aria-label="Photo of a two-storey house roofed under scaffolding"></div>
  <div class="work-title" style="left:132px">Heading 1</div>
  <div class="work-photo" style="left:448px;background:linear-gradient(90deg,#2c2f33,#3a3d40 40%,#9aa77f 70%,#6c8b4c)" role="img" aria-label="Photo of a dark clad building beside a muddy site"></div>
  <div class="work-title" style="left:448px">Heading 2</div>
  <div class="work-photo" style="left:767px;background:linear-gradient(180deg,#5a5c60,#26282b 45%,#a7886a 70%,#3a3a36)" role="img" aria-label="Photo of an open steel shed at sunset"></div>
  <div class="work-title" style="left:767px">Heading 3</div>
</section>

<footer class="site-footer">
  <div class="foot-label" style="left:133px;top:50px">Contact Us</div>
  <div class="contact-item" style="left:138px">
    <svg width="16" height="16" viewBox="0 0 24 24" style="margin-top:14px"><path fill="#fff" d="M6.6 10.8a15 15 0 006.6 6.6l2.2-2.2c.3-.3.7-.4 1-.2 1.1.4 2.3.6 3.6.6.6 0 1 .4 1 1V20c0 .6-.4 1-1 1C10.6 21 3 13.4 3 4c0-.6.4-1 1-1h3.5c.6 0 1 .4 1 1 0 1.3.2 2.5.6 3.6.1.3 0 .7-.2 1z"/></svg>
    <div><small>CALL US :</small><span>021 555 01234</span></div>
  </div>
  <div class="contact-item" style="left:378px">
    <svg width="20" height="16" viewBox="0 0 20 16" style="margin-top:6px"><rect width="20" height="16" rx="2" fill="#fff"/><path d="M1 2l9 7 9-7" fill="none" stroke="#474747" stroke-width="1.8"/></svg>
    <div><small>E MAIL US :</small><span>hello@brambleroofing.co.nz</span></div>
  </div>
  <div class="badge" role="img" aria-label="Certified Trade Craftsman badge"></div>
  <div class="foot-label" style="left:133px;top:190px">Menu</div>
  <div class="foot-menu"><a href="#">HOME</a><i>|</i><a href="#">WHAT WE DO</a><i>|</i><a href="#">WHO WE ARE</a><i>|</i><a href="#">SERVICES</a><i>|</i><a href="#">OUR WORK</a><i>|</i><a href="#">CONTACT</a></div>
  <div class="foot-rule"></div>
  <div class="foot-brand"><span class="brand-mark"></span><span class="brand-name">Bramble Roofing</span></div>
  <div class="follow">FOLLOW US <a class="social" href="#" aria-label="Social page"></a></div>
  <div class="copyright">Copyrights @ 2017 all rights reserved</div>
</footer>

</body>
</html>
```